Redesign Website - Current one too plain

The description is in the uploaded file. Please let me know if you need any more information. I'd prefer it if someone could implement the design to a WordPress site but the best design will win, regardless.
I would like the forms to look nice as well
UPDATE:
I don't think we can use the images that I provided, I think they make the site look a bit 'cheap' and I really don't know how to replace them. One thought I have had is to make the "Simple, Unique, Effective" a second feature on the right side of the page with the search on the left
Target Market(s)
Small companies, private sellers of cars and people who rent their caravan/holiday home out
Industry/Entity Type
Advertising
Number of Pages Required
3 page
Colors
Designer to choose colors to be used in the design.
Look and feel

```html
<!DOCTYPE html>
<html lang="en">
<head>
<meta charset="utf-8">
<title>Plakko – How it works</title>
<link rel="stylesheet" href="https://fonts.googleapis.com/css2?family=Inter:wght@400;500;600&family=Poppins:wght@400;500;600&display=swap">
<style>
:root{
  --bg:#232323;
  --footer:#141414;
  --lime:#e9fd55;
  --lime-text:#e2f54c;
  --ink:#111111;
  --white:#ffffff;
  --muted:#c9c9c9;
  --field:#2a2a2a;
  --placeholder:#8a8a8a;
}
*{box-sizing:border-box;margin:0;padding:0}
html,body{width:1200px;height:2521px;overflow:hidden;background:var(--bg)}
body{position:relative;font-family:"Inter",sans-serif;color:var(--white)}
.abs{position:absolute}
.section-title{left:98px;top:30px;font-size:25px;font-weight:500;color:var(--lime-text)}
.steps-copy{left:98px;width:470px;font-size:16.5px;line-height:28.4px}
.step-card{width:180px;text-align:center;font-size:16.5px;line-height:28.4px}
.step-icon{width:76px;height:76px;border-radius:14px;background:var(--lime);margin:0 auto 2px;display:flex;align-items:center;justify-content:center;color:var(--ink)}
.step-icon .code{font-size:44px;font-weight:600;letter-spacing:-1px}
.vehicles{left:88px;top:724px;width:1038px;height:343px;border-radius:40% 40% 30% 30%/30% 30% 20% 20%;background:radial-gradient(ellipse at 50% 50%,#cfcfcf 0%,#9a9a9a 45%,#3a3a3a 80%,var(--bg) 100%)}
.why{left:57px;top:1152px;width:1086px;height:397px;border-radius:30px;background:var(--lime);color:var(--ink)}
.why h2{position:absolute;top:50px;width:100%;text-align:center;font-size:27px;font-weight:500}
.why .body{position:absolute;left:65px;top:143px;width:960px;font-size:16.5px;line-height:28.4px}
.why ul{padding-left:25px}
.cta-title{left:0;top:1607px;width:1200px;text-align:center;font-size:27px;font-weight:500}
.cta-text{left:135px;top:1701px;width:920px;font-size:16.5px;line-height:28.4px}
.cta-btn{left:482px;top:1831px;width:238px;height:35px;border-radius:18px;background:var(--lime);color:var(--ink);font-size:16.5px;display:flex;align-items:center;justify-content:center}
.site-footer{left:0;top:1927px;width:1200px;height:594px;background:var(--footer);font-family:"Poppins",sans-serif}
.f-head{font-size:15px;font-weight:500}
.f-link{font-size:13.5px;color:var(--muted)}
.contact-row{display:flex;align-items:center;gap:8px;font-size:13.5px;color:var(--muted)}
.social{width:28px;height:28px;border-radius:50%}
.store{width:87px;height:25px;border:1px solid #555;border-radius:4px;background:#000}
.field-label{font-size:13.5px;color:var(--muted)}
.field{left:839px;width:246px;border-radius:6px;background:var(--field);font-size:11.5px;color:var(--placeholder);padding:13px 13px}
.send{left:982px;top:2424px;width:103px;height:31px;border-radius:16px;background:var(--lime);color:var(--ink);font-size:14px;font-weight:500;display:flex;align-items:center;justify-content:center}
</style>
</head>
<body>

<h1 class="abs section-title">How it works</h1>

<p class="abs steps-copy" style="top:115px">Step 1:</p>
<p class="abs steps-copy" style="top:172px">Generate your unique code and create an eye-catching advert showcasing your business, products, services, and contact details.</p>
<p class="abs steps-copy" style="top:286px">Step 2:</p>
<p class="abs steps-copy" style="top:342px">Affix your code prominently on vehicles like cars, vans, or caravans, acting as a beacon to guide interested customers to your doorstep.</p>
<p class="abs steps-copy" style="top:456px">Step 3:</p>
<p class="abs steps-copy" style="top:513px">Effortlessly connect with potential customers using your memorable code, increasing visibility and expanding your customer base.</p>

<div class="abs step-card" style="left:594px;top:130px">
  <div class="step-icon">
    <svg width="44" height="40" viewBox="0 0 44 40" fill="none" stroke="#111" stroke-width="2"><rect x="2" y="2" width="28" height="24" rx="2"/><line x1="2" y1="8" x2="30" y2="8"/><rect x="8" y="12" width="14" height="10"/><circle cx="30" cy="30" r="7"/><circle cx="38" cy="34" r="4"/></svg>
  </div>
  <div>Step 1:<br>Create Your<br>Advert Content</div>
</div>

<svg class="abs" style="left:755px;top:165px" width="95" height="85" viewBox="0 0 95 85" fill="none" stroke="#fff" stroke-width="5" stroke-linecap="round" stroke-linejoin="round"><path d="M5 10 C45 5 75 30 85 75"/><path d="M68 68 L85 78 L92 58"/></svg>

<div class="abs step-card" style="left:770px;top:290px">
  <div class="step-icon"><span class="code">A1</span></div>
  <div>Step 2:<br>Display Your<br>Code Content</div>
</div>

<svg class="abs" style="left:855px;top:488px" width="115" height="62" viewBox="0 0 115 62" fill="none" stroke="#fff" stroke-width="5" stroke-linecap="round" stroke-linejoin="round"><path d="M8 6 C25 40 60 52 105 48"/><path d="M90 32 L107 48 L92 62"/></svg>

<div class="abs step-card" style="left:947px;top:481px">
  <div class="step-icon">
    <svg width="46" height="40" viewBox="0 0 46 40" fill="none" stroke="#111" stroke-width="2"><rect x="2" y="8" width="22" height="12" rx="2"/><circle cx="8" cy="14" r="1.2" fill="#111"/><circle cx="13" cy="14" r="1.2" fill="#111"/><circle cx="18" cy="14" r="1.2" fill="#111"/><rect x="22" y="2" width="20" height="12" rx="2"/><line x1="26" y1="6" x2="38" y2="6"/><line x1="26" y1="10" x2="36" y2="10"/><rect x="2" y="24" width="24" height="12" fill="#111"/><path d="M32 36 V28 L36 22 V28 H42 V36 Z" fill="#111"/></svg>
  </div>
  <div>Step 3:<br>Customers Find<br>Your Content</div>
</div>

<div class="abs vehicles" role="img" aria-label="Silver SUV, static caravan and silver work van showing where codes can be displayed"></div>

<section class="abs why">
  <h2>Why Choose Us</h2>
  <div class="body">
    <p>Our platform offers a user-friendly experience that empowers businesses of all sizes to increase their presence. With our easy-to-use system and eye-catching codes, you can enjoy these benefits:</p>
    <ul>
      <li>Stand out from competitors with a unique identifier</li>
      <li>Attract more customers with straightforward access to your business</li>
      <li>Increase your brand recognition and credibility</li>
      <li>Track the effectiveness of your adverts with real-time data</li>
    </ul>
  </div>
</section>

<h2 class="abs cta-title">Ready to Elevate Your Business?</h2>
<p class="abs cta-text">Don't miss out on this opportunity to simplify and optimize your customer connections. Sign up now and start displaying your code to grow your business and build stronger customer relationships.</p>
<div class="abs cta-btn">Sign up now</div>

<footer class="abs site-footer">
  <div class="abs f-head" style="left:114px;top:66px">Plakko</div>
  <div class="abs f-link" style="left:114px;top:106px">Home</div>
  <div class="abs f-link" style="left:114px;top:132px">Advertise</div>
  <div class="abs f-link" style="left:114px;top:160px">Register</div>

  <div class="abs f-head" style="left:297px;top:66px">Rules</div>
  <div class="abs f-link" style="left:297px;top:106px">FAQs</div>
  <div class="abs f-link" style="left:297px;top:132px">Terms and Conditions</div>
  <div class="abs f-link" style="left:297px;top:160px">Privacy Policy</div>

  <div class="abs f-head" style="left:534px;top:66px">Contact Us</div>
  <div class="abs contact-row" style="left:534px;top:108px">
    <svg width="18" height="14" viewBox="0 0 18 14" fill="none" stroke="#e9fd55" stroke-width="1.5"><rect x="1" y="1" width="16" height="12" rx="2"/><path d="M1 3 L9 8 L17 3"/></svg>hello@plakko.example</div>
  <div class="abs contact-row" style="left:534px;top:140px">
    <svg width="18" height="18" viewBox="0 0 24 24" fill="none" stroke="#e9fd55" stroke-width="1.8"><path d="M5 3h4l2 5-3 2a12 12 0 0 0 6 6l2-3 5 2v4a2 2 0 0 1-2 2A18 18 0 0 1 3 5a2 2 0 0 1 2-2z"/></svg>+ 91 0100 555 789</div>
  <div class="abs contact-row" style="left:534px;top:173px">
    <svg width="18" height="18" viewBox="0 0 24 24" fill="none" stroke="#e9fd55" stroke-width="1.8"><path d="M12 22s7-7 7-12a7 7 0 0 0-14 0c0 5 7 12 7 12z"/><circle cx="12" cy="10" r="2.5"/></svg>123, Random Street, Random</div>

  <div class="abs f-head" style="left:534px;top:209px">Social Media</div>
  <div class="abs social" style="left:533px;top:249px;background:#1877f2"></div>
  <div class="abs social" style="left:571px;top:249px;background:#e1306c"></div>
  <div class="abs social" style="left:610px;top:249px;background:#1da1f2"></div>
  <div class="abs social" style="left:649px;top:249px;background:#25a244"></div>

  <div class="abs f-head" style="left:534px;top:293px">Download The App</div>
  <div class="abs store" style="left:539px;top:332px"></div>
  <div class="abs store" style="left:631px;top:332px"></div>

  <div class="abs f-head" style="left:839px;top:66px">Or Connect With Us Here!</div>
  <div class="abs field-label" style="left:839px;top:104px">Your Email</div>
  <div class="abs field" style="top:140px;height:46px">Enter Your Email</div>
  <div class="abs field-label" style="left:839px;top:202px">Your Phone Number</div>
  <div class="abs field" style="top:239px;height:45px">Enter Your Phone Number</div>
  <div class="abs field-label" style="left:839px;top:301px">Your Issue</div>
  <div class="abs field" style="top:336px;height:131px">Briefly describe your issue</div>
</footer>
<div class="abs send">Send</div>

</body>
</html>
```